Hi Tech startup needs an investor presentation

We need an investor presentaiton for a new company based in Russia. We develop innovative solutions connecting customers and businesses via VoIP. Our initial product is an iPhone / Android app connecting customers directly to call centers / help desks bypassing calling (800) numbers. This also saves money for companies who do not need to pay for (800) lines.
Updates

Hi guys!

I have now made the contest committed, so please participate.

Industry/Entity Type

It Company

Requirements
Must have
• The ppt must follow the structure already suggested in the uploaded ppt
Nice to have
• Some nice graphic solutions, pictograms and so on instead of large chunks of text
Should not have
• Should not use old-style fonts and solutions.
• Also, not too cocky please.

```html
<!DOCTYPE html>
<html lang="en">
<head>
<meta charset="utf-8">
<title>Who we are and what we believe</title>
<link href="https://fonts.googleapis.com/css2?family=Titillium+Web:wght@400;600;700&display=swap" rel="stylesheet">
<style>
  :root {
    --yellow-light: #ffd84a;
    --yellow: #f9c316;
    --yellow-deep: #f2a900;
    --ink: #2b2118;
    --ink-soft: #3d3127;
    --card-border: #efe3c4;
    --card-shadow: rgba(120, 95, 40, 0.22);
    --white: #ffffff;
    --photo-blue: #bcd7ee;
    --photo-grey: #d9dce1;
  }
  * { box-sizing: border-box; margin: 0; padding: 0; }
  html, body { width: 1200px; height: 900px; overflow: hidden; background: var(--white); }
  body { font-family: "Titillium Web", Arial, sans-serif; color: var(--ink); position: relative; }

  .slide-header {
    position: absolute; left: 0; top: 0; width: 1200px; height: 88px;
    background: linear-gradient(90deg, var(--yellow-deep) 0%, var(--yellow) 35%, var(--yellow-light) 100%);
    border-bottom: 4px solid var(--ink);
  }
  .slide-title {
    position: absolute; left: 34px; top: 18px;
    font-size: 37px; font-weight: 700; color: var(--ink); letter-spacing: 0.2px;
  }

  .card {
    position: absolute; left: 48px;
    background: var(--white);
    border: 1px solid var(--card-border);
    border-radius: 14px;
    box-shadow: 2px 4px 6px var(--card-shadow);
  }
  .card-setup { top: 123px; width: 1128px; height: 180px; }
  .card-phone { top: 363px; width: 1100px; height: 176px; }
  .card-savings { top: 588px; width: 1128px; height: 180px; }

  .step-badge {
    position: absolute; width: 66px; height: 66px; border-radius: 50%;
    background: radial-gradient(circle at 40% 35%, var(--yellow-light), var(--yellow-deep));
    border: 3px solid var(--ink-soft);
    box-shadow: 0 0 0 3px var(--white), 1px 3px 5px var(--card-shadow);
    display: flex; align-items: center; justify-content: center;
    font-size: 40px; font-weight: 700; color: var(--ink); line-height: 1;
  }
  .badge-1 { left: 19px; top: 169px; }
  .badge-2 { left: 1108px; top: 420px; }
  .badge-3 { left: 13px; top: 630px; }

  .visual { position: absolute; border-radius: 8px; }
  .visual-devices { left: 95px; top: 130px; width: 310px; height: 162px;
    background: linear-gradient(135deg, var(--photo-blue), var(--photo-grey)); }
  .visual-call { left: 600px; top: 378px; width: 500px; height: 160px;
    background: linear-gradient(90deg, var(--photo-grey), var(--photo-blue) 50%, var(--photo-grey)); }
  .visual-relax { left: 80px; top: 596px; width: 370px; height: 168px;
    background: linear-gradient(135deg, var(--photo-grey), var(--photo-blue)); }

  .card-heading { font-size: 22px; font-weight: 600; color: var(--ink); line-height: 1.2; }
  .bullet-list { list-style: none; margin-top: 6px; }
  .bullet-list li {
    position: relative; padding-left: 28px;
    font-size: 18px; line-height: 1.42; color: var(--ink);
  }
  .bullet-list li svg { position: absolute; left: 4px; top: 7px; }

  .setup-text { position: absolute; left: 412px; top: 134px; width: 760px; }
  .setup-text .bullet-list li { margin-bottom: 3px; }
  .phone-text { position: absolute; left: 68px; top: 370px; width: 540px; }
  .phone-text .bullet-list li { margin-bottom: 2px; }

  .savings-text {
    position: absolute; left: 480px; top: 655px; width: 630px; text-align: center;
    font-size: 27px; font-weight: 600; color: var(--ink-soft);
  }

  .slide-footer {
    position: absolute; left: 0; top: 822px; width: 1200px; height: 78px;
    background: linear-gradient(90deg, var(--yellow-deep) 0%, var(--yellow) 40%, var(--yellow-light) 100%);
    border-top: 4px solid var(--ink);
  }
  .page-number {
    position: absolute; left: 9px; top: 838px; width: 48px; height: 48px; border-radius: 50%;
    background: var(--ink); color: var(--white);
    display: flex; align-items: center; justify-content: center;
    font-size: 19px; font-weight: 600;
  }
  .copyright { position: absolute; left: 81px; top: 847px; font-size: 20px; color: var(--ink); }

  .brand { position: absolute; left: 890px; top: 794px; height: 100px; display: flex; align-items: center; gap: 14px; }
  .brand-dot {
    width: 96px; height: 96px; border-radius: 50%;
    background: var(--yellow); border: 5px solid var(--white);
    box-shadow: 0 2px 6px var(--card-shadow);
  }
  .brand-name { font-size: 50px; font-weight: 400; color: var(--ink-soft); margin-top: 40px; letter-spacing: 0.5px; }
</style>
</head>
<body>
  <header class="slide-header">
    <h1 class="slide-title">Who we are and what we believe</h1>
  </header>

  <section class="card card-setup"></section>
  <div class="visual visual-devices" role="img" aria-label="Smartphone and laptop syncing with a cloud"></div>
  <div class="setup-text">
    <h2 class="card-heading">Easy installation and set up process</h2>
    <ul class="bullet-list">
      <li><svg width="10" height="14" viewBox="0 0 10 14"><path d="M2 1 L8 7 L2 13" fill="none" stroke="#2b2118" stroke-width="3"/></svg>Quick and easy;</li>
      <li><svg width="10" height="14" viewBox="0 0 10 14"><path d="M2 1 L8 7 L2 13" fill="none" stroke="#2b2118" stroke-width="3"/></svg>Free;</li>
      <li><svg width="10" height="14" viewBox="0 0 10 14"><path d="M2 1 L8 7 L2 13" fill="none" stroke="#2b2118" stroke-width="3"/></svg>CallWay means no need to use your phone memory, the information is downloaded into your phone every time through could solutions</li>
    </ul>
  </div>
  <div class="step-badge badge-1">1</div>

  <section class="card card-phone"></section>
  <div class="visual visual-call" role="img" aria-label="Businessman and woman on phones connected through a cloud"></div>
  <div class="phone-text">
    <h2 class="card-heading">All the information you need is in your phone!</h2>
    <ul class="bullet-list">
      <li><svg width="10" height="14" viewBox="0 0 10 14"><path d="M2 1 L8 7 L2 13" fill="none" stroke="#2b2118" stroke-width="3"/></svg>Rateo-style content;</li>
      <li><svg width="10" height="14" viewBox="0 0 10 14"><path d="M2 1 L8 7 L2 13" fill="none" stroke="#2b2118" stroke-width="3"/></svg>Easy navigation between companies / departments;</li>
      <li><svg width="10" height="14" viewBox="0 0 10 14"><path d="M2 1 L8 7 L2 13" fill="none" stroke="#2b2118" stroke-width="3"/></svg>Problem evaluation forms to direct you to the right desk;</li>
      <li><svg width="10" height="14" viewBox="0 0 10 14"><path d="M2 1 L8 7 L2 13" fill="none" stroke="#2b2118" stroke-width="3"/></svg>One-click connection</li>
    </ul>
  </div>
  <div class="step-badge badge-2">2</div>

  <section class="card card-savings"></section>
  <div class="visual visual-relax" role="img" aria-label="Man relaxing in a chair beside a clock and a sunny landscape frame"></div>
  <p class="savings-text">Start enjoying the time and money you have saved!</p>
  <div class="step-badge badge-3">3</div>

  <footer class="slide-footer"></footer>
  <div class="page-number">01</div>
  <p class="copyright">Copyright text here</p>
  <div class="brand">
    <span class="brand-dot"></span>
    <span class="brand-name">nexlink</span>
  </div>
</body>
</html>
```